IT Services

We come to you
Only $49/hr
No contract, no monthly fee
Software engineer on staff
remote assistance or visit in your office

On the back of the card I want to list services.

- Server setup
- Network troubleshooting
- Printer setup
- Secure backup setup
- Software installation
- Wireless network setup
- Wired network setup
- Disaster recovery
- Website management
- Any other technology related support
- Email setup
- HIPAA compliance review and setup
Updates

the URL is: GEARFIXPRO.ZONE please use it on the card

On the card we need to mention "Connect remotely to address your IT issues" if there is enough room as well as "we go to you"

Industry/Entity Type

Printer

Contact Information for Business Card

I want a busoiness card to offer my services to doctor offices, it can be dentists, Otamatry, and other professions. I provide the following service. My plan is to go to their office and drop off my card. I don't want them to forget about it that is why I am paying for the design. I like hand writing design formats.

```html
<!DOCTYPE html>
<html lang="en">
<head>
<meta charset="utf-8">
<title>GEARFIXPRO.ZONE – Business Card</title>
<link href="https://fonts.googleapis.com/css2?family=Open+Sans:wght@300;400&family=Dancing+Script:wght@400;500&display=swap" rel="stylesheet">
<style>
  :root {
    --bg: #e9e6e1;
    --blue-deep: #1a8fc4;
    --blue-bright: #3fb3e3;
    --blue-pale: #cfe9f6;
    --blue-text: #4fa9d6;
    --ink: #3a3d40;
    --white: #ffffff;
    --card-white: #f4f6f8;
  }
  * { margin: 0; padding: 0; box-sizing: border-box; }
  html, body { width: 704px; height: 1200px; overflow: hidden; background: var(--bg); }
  .canvas { position: relative; width: 704px; height: 1200px; }

  .card {
    position: absolute;
    left: 72px;
    width: 560px;
    height: 320px;
    border-radius: 14px;
    overflow: hidden;
    background: var(--card-white);
    box-shadow: 0 10px 24px rgba(0,0,0,.18);
  }
  .card-front { top: 140px; }
  .card-back  { top: 740px; }
  .card svg.card-art { position: absolute; inset: 0; }

  /* front */
  .brand {
    position: absolute; left: 36px; top: 40px;
    display: flex; align-items: center; gap: 14px;
    font-family: "Open Sans", sans-serif; font-weight: 300;
    font-size: 32px; letter-spacing: .5px; color: var(--white);
  }
  .brand-mark { width: 26px; height: 26px; background: var(--white); opacity: .9; }
  .offer {
    position: absolute; left: 40px; top: 168px;
    font-family: "Dancing Script", cursive; font-size: 21px; line-height: 26px;
    color: var(--ink); list-style: none;
  }
  .offer .lead { color: var(--blue-text); }

  /* back */
  .owner {
    position: absolute; left: 40px; top: 26px;
    font-family: "Open Sans", sans-serif;
  }
  .owner-name { font-size: 24px; font-weight: 300; color: var(--blue-text); }
  .owner-site { font-size: 13px; color: var(--ink); }
  .contact {
    position: absolute; right: 32px; top: 30px; text-align: right;
    font-family: "Open Sans", sans-serif; font-size: 13px; color: var(--ink); line-height: 22px;
  }
  .contact-icons { display: flex; justify-content: flex-end; gap: 6px; margin-bottom: 4px; }
  .icon-square { width: 11px; height: 11px; background: var(--blue-deep); border-radius: 2px; }
  .icon-circle { width: 11px; height: 11px; background: var(--blue-deep); border-radius: 50%; }
  .services {
    position: absolute; left: 36px; top: 150px; width: 500px;
    columns: 2; column-gap: 24px;
    font-family: "Dancing Script", cursive; font-size: 18px; line-height: 25px;
    color: var(--white); list-style: none;
  }
</style>
</head>
<body>
<main class="canvas">

  <section class="card card-front" aria-label="Card front">
    <svg class="card-art" width="560" height="320" viewBox="0 0 560 320" aria-hidden="true">
      <defs>
        <linearGradient id="frontBlue" x1="0" y1="0" x2="1" y2="1">
          <stop offset="0" stop-color="#1a8fc4"/>
          <stop offset="1" stop-color="#3fb3e3"/>
        </linearGradient>
      </defs>
      <path d="M0 0 H560 V70 C430 90 300 130 0 178 Z" fill="#cfe9f6"/>
      <path d="M0 0 H560 V44 C420 70 300 105 0 150 Z" fill="url(#frontBlue)"/>
      <rect class="faint-square" x="410" y="90" width="110" height="110" fill="#cfe9f6" opacity=".6"/>
    </svg>
    <div class="brand"><span class="brand-mark"></span>GEARFIXPRO.ZONE</div>
    <ul class="offer">
      <li class="lead">We come to you</li>
      <li>Only $49/hr</li>
      <li>No contract, no monthly fee</li>
      <li>Software engineer on staff</li>
      <li>remote assistance or visit in your office</li>
    </ul>
  </section>

  <section class="card card-back" aria-label="Card back">
    <svg class="card-art" width="560" height="320" viewBox="0 0 560 320" aria-hidden="true">
      <defs>
        <linearGradient id="backBlue" x1="0" y1="0" x2="1" y2="1">
          <stop offset="0" stop-color="#3fb3e3"/>
          <stop offset="1" stop-color="#1a8fc4"/>
        </linearGradient>
      </defs>
      <rect class="faint-square" x="200" y="14" width="110" height="110" fill="#cfe9f6" opacity=".5"/>
      <rect x="0" y="134" width="560" height="186" fill="url(#backBlue)"/>
    </svg>
    <div class="owner">
      <p class="owner-name">Dana Wexler</p>
      <p class="owner-site">fixdesk.support</p>
    </div>
    <div class="contact">
      <div class="contact-icons"><span class="icon-square"></span><span class="icon-circle"></span></div>
      <p>1-800-555-0142</p>
      <p>GEARFIXPRO.ZONE</p>
    </div>
    <ul class="services">
      <li>Server setup</li>
      <li>Network troubleshooting</li>
      <li>Printer setup</li>
      <li>Secure backup setup</li>
      <li>Software installation</li>
      <li>Wireless network setup</li>
      <li>Wired network setup</li>
      <li>Disaster recovery</li>
      <li>Website management</li>
      <li>Any other technology related support</li>
      <li>Email setup</li>
      <li>HIPAA compliance review and setup</li>
    </ul>
  </section>

</main>
</body>
</html>
```